Bright Harbor Design

We need a web design for our startup company based in Zurich, Switzerland called Bright Harbor. We offer professional flirt and dating advice, self development with seminars and practical coachings.

The final website aims for two capital goals. First, it will contain text, pictures and video based content presenting and advertising our services. Furthermore, we want to bind our costumers with a plattform offering them to share their expiriences related with our services.

The targeted group will be men from 25 to 40 years.
Updates

The design requires also a register-box to put in the clients Name and Email

I need (besides of the "email registration box") a "Video Gallery", "Blog" and "Agenda (with the next events to come)"

Target Market(s)

Guys around 25 to 40 years who want to improve their social lifestyle

Industry/Entity Type

Advertising

Requirements
Must have
• First and foremost, the design must transfer strong emotions and suggest an attractive social lifestyle.

The design should not be overloaded with content but should include pictures, videos and text.

The design should present a modern, urban lifestyle.
Nice to have
• There is a logo attached to the assignement. However, if you have a good idea for an improved or different logo, please do not hesitate to design your ideas.

```html
<!DOCTYPE html>
<html lang="en">
<head>
<meta charset="utf-8">
<title>Bright Harbor – Self development, flirt and dating advice</title>
<link href="https://fonts.googleapis.com/css2?family=Open+Sans:ital,wght@0,300;0,400;0,600;0,700;1,700&display=swap" rel="stylesheet">
<style>
:root{
  --green:#11916f;
  --green-dark:#0c7a5d;
  --ink:#4a4a4a;
  --muted:#777;
  --panel:#efefef;
  --footer:#7b7b7b;
  --footer-dark:#575757;
  --field:#5a5a5a;
  --white:#fff;
}
*{box-sizing:border-box;margin:0;padding:0}
html,body{width:875px;height:1200px;overflow:hidden}
body{position:relative;font-family:'Open Sans',Arial,sans-serif;color:var(--ink);background:var(--white)}
.abs{position:absolute}

/* header */
.site-header{left:0;top:0;width:875px;height:52px;background:#fafafa;z-index:3;box-shadow:0 1px 3px rgba(0,0,0,.15);overflow:hidden}
.brand{left:96px;top:15px;display:flex;align-items:center;gap:8px;font-weight:700;font-size:15px;color:var(--green)}
.brand-dot{width:20px;height:20px;border-radius:50%;background:var(--green)}
.nav a{position:absolute;top:21px;font-size:9.5px;color:#444;text-decoration:none;white-space:nowrap}
.nav-active{left:448px;top:44px;width:52px;height:52px;border-radius:50%;background:var(--green)}

/* hero */
.hero{left:0;top:52px;width:875px;height:458px;background:linear-gradient(100deg,#8a9bab 0%,#b7a79a 30%,#c9b3a3 45%,#5c5358 62%,#2d2a31 80%,#4a4550 100%)}
.hero-shade{left:0;top:52px;width:875px;height:458px;background:linear-gradient(180deg,rgba(0,0,0,.1),rgba(0,0,0,.25))}
.hero-mark{left:0;width:875px;top:100px;text-align:center;color:var(--white);font-size:16px;font-weight:600}
.hero-title{left:0;width:875px;top:136px;text-align:center;color:var(--white);font-weight:300;font-size:31px;line-height:38px}
.hero-title em{font-weight:700;font-style:italic}
.hero-sub{left:0;width:875px;top:255px;text-align:center;color:rgba(255,255,255,.85);font-size:19px;font-weight:300}
.hero-sub b{font-weight:600;color:var(--white)}
.register{left:197px;top:335px;width:481px;height:51px;background:var(--white);border-radius:5px;box-shadow:0 2px 6px rgba(0,0,0,.25)}
.register .field{position:absolute;top:14px;width:160px;height:23px;border:1px solid #ccc;border-radius:5px;background:#eee;font-size:10px;color:#999;padding:4px 9px}
.register .btn{position:absolute;left:365px;top:13px;width:102px;height:25px;border-radius:5px;background:var(--green);color:var(--white);font-size:10px;font-weight:600;text-align:center;line-height:25px}
.scroll-label{left:0;width:875px;top:423px;text-align:center;color:rgba(255,255,255,.8);font-size:10.5px}

/* sections */
.blog-col{left:586px;top:510px;width:289px;height:526px;background:var(--panel)}
.agenda-bg{left:0;top:799px;width:586px;height:237px;background:var(--panel)}
.section-title{font-size:20px;font-weight:600;color:#555;letter-spacing:.3px}
.section-link{font-size:10px;color:var(--green);font-weight:600;display:flex;align-items:center;gap:6px}
.card-title{font-size:11.5px;font-weight:700;color:var(--green);line-height:14px}
.card-text{font-size:9.6px;color:#777;line-height:12px}
.read-more{width:57px;height:18px;border-radius:3px;background:var(--green);color:var(--white);font-size:9.5px;text-align:center;line-height:18px}

.video{width:218px;height:153px;background:#050505}
.video-tools{position:absolute;right:8px;top:6px;display:flex;flex-direction:column;gap:4px}
.video-tool{width:30px;height:24px;background:#2a2a2a;border-radius:2px;color:var(--white);font-size:5.5px;font-weight:700;display:flex;flex-direction:column;align-items:center;padding-top:3px;gap:1px;line-height:7px}
.video-tool svg{display:block}
.video-bar{position:absolute;left:8px;right:8px;bottom:8px;height:24px;background:#1d1d1d;border-radius:2px}

.event{width:217px;height:82px;background:#c7d3db}
.event-date{position:absolute;left:0;top:0;width:90px;height:82px;background:var(--green);color:var(--white);text-align:center}
.event-date .day{font-size:30px;font-weight:300;line-height:34px;margin-top:10px}
.event-date .month{font-size:13px}
.event-photo{position:absolute;left:90px;top:0;width:127px;height:82px}

.blog-photo{width:171px;height:98px}

/* footer */
.footer{left:0;top:1036px;width:875px;height:126px;background:var(--footer)}
.footer h4{position:absolute;font-size:12px;font-weight:400;color:var(--white)}
.footer .link{position:absolute;font-size:10px;color:var(--white)}
.footer .input{position:absolute;height:20px;background:var(--field);border:1px solid #444;border-radius:3px;font-size:8.5px;color:var(--white);padding:3px 7px}
.send{left:689px;top:92px;width:59px;height:20px;border-radius:4px;background:#f4f4f4;color:#555;font-size:10px;text-align:center;line-height:20px}
.copyright{left:0;top:1162px;width:875px;height:38px;background:var(--footer-dark);color:var(--white);font-size:9.5px;text-align:center;line-height:38px}
</style>
</head>
<body>

<header class="abs site-header">
  <div class="abs brand"><span class="brand-dot"></span>Bright Harbor</div>
  <div class="abs nav-active"></div>
  <nav class="nav">
    <a style="left:457px">Services</a>
    <a style="left:512px">About Us</a>
    <a style="left:571px">Agenda</a>
    <a style="left:624px">Video Gallery</a>
    <a style="left:706px">Blog</a>
    <a style="left:743px">Contacts</a>
  </nav>
</header>

<section>
  <div class="abs hero" role="img" aria-label="Photo of a young couple sitting close together in a city setting"></div>
  <div class="abs hero-shade"></div>
  <div class="abs hero-mark">Bright Harbor</div>
  <h1 class="abs hero-title">Self development, flirt and dating advice with<br><em>Bright Harbor...</em></h1>
  <p class="abs hero-sub">Share your <b>experience</b> - register for <b>FREE</b>!</p>
  <svg class="abs" style="left:232px;top:290px" width="411" height="16" viewBox="0 0 411 16">
    <path d="M0 4H195L205 14L215 4H411" fill="none" stroke="rgba(255,255,255,.55)" stroke-width="1"/>
  </svg>
  <form class="abs register">
    <div class="field" style="left:14px">Name</div>
    <div class="field" style="left:189px">E-Mail</div>
    <div class="btn">REGISTER</div>
  </form>
  <div class="abs scroll-label">Scroll down</div>
  <svg class="abs" style="left:427px;top:442px" width="22" height="42" viewBox="0 0 22 42">
    <rect x="1" y="1" width="20" height="34" rx="10" fill="#fff"/>
    <rect x="8.5" y="8" width="5" height="10" rx="2.5" fill="none" stroke="#888" stroke-width="1.3"/>
    <path d="M8 36l3 4 3-4z" fill="#fff"/>
  </svg>
</section>

<div class="abs blog-col"></div>
<div class="abs agenda-bg"></div>

<!-- video gallery -->
<h2 class="abs section-title" style="left:96px;top:527px">VIDEO GALLERY</h2>
<div class="abs section-link" style="left:500px;top:533px">
  <svg width="13" height="10" viewBox="0 0 13 10"><circle cx="4" cy="2.5" r="2.3" fill="currentColor"/><circle cx="9.5" cy="3" r="2" fill="currentColor"/><path d="M0 10c0-3 1.8-4.5 4-4.5S8 7 8 10zM8.5 10c0-2 .5-3.8 1.8-4.2 1.6 0 2.7 1.6 2.7 4.2z" fill="currentColor"/></svg>All videos
</div>

<div class="abs video" style="left:96px;top:568px">
  <div class="video-tools">
    <div class="video-tool"><svg width="11" height="10" viewBox="0 0 12 11"><path d="M6 10.5L1.2 5.8C-.4 4.2.3 1 3 1c1.3 0 2.3.8 3 1.8C6.7 1.8 7.7 1 9 1c2.7 0 3.4 3.2 1.8 4.8z" fill="#fff"/></svg>LIKE</div>
    <div class="video-tool"><svg width="10" height="10" viewBox="0 0 10 10"><circle cx="5" cy="5" r="4.2" fill="none" stroke="#fff" stroke-width="1.3"/><path d="M5 2.5V5l1.8 1.3" fill="none" stroke="#fff" stroke-width="1.2"/></svg>LATER</div>
    <div class="video-tool"><svg width="11" height="10" viewBox="0 0 11 10"><circle cx="2" cy="5" r="1.6" fill="#fff"/><circle cx="9" cy="1.8" r="1.6" fill="#fff"/><circle cx="9" cy="8.2" r="1.6" fill="#fff"/><path d="M2 5L9 1.8M2 5l7 3.2" stroke="#fff" stroke-width="1"/></svg>SHARE</div>
  </div>
  <div class="video-bar">
    <svg width="202" height="24" viewBox="0 0 202 24"><rect x="12" y="7" width="3" height="10" fill="#fff"/><rect x="18" y="7" width="3" height="10" fill="#fff"/><rect x="42" y="2" width="26" height="9" fill="#fff"/><text x="44" y="9" font-size="6.5" font-family="Open Sans, sans-serif">00:00</text><rect x="42" y="13" width="86" height="5" fill="none" stroke="#666"/><g fill="#666"><rect x="132" y="9" width="1.5" height="8"/><rect x="135" y="9" width="1.5" height="8"/><rect x="138" y="9" width="1.5" height="8"/><rect x="141" y="9" width="1.5" height="8"/><rect x="144" y="9" width="1.5" height="8"/></g><text x="150" y="16" font-size="9" font-weight="700" font-style="italic" fill="#666" font-family="Open Sans, sans-serif">HD</text><path d="M176 8h3M176 8v3M186 8h-3M186 8v3M176 17h3M176 17v-3M186 17h-3M186 17v-3" stroke="#fff" stroke-width="1.4"/></svg>
  </div>
</div>
<div class="abs video" style="left:343px;top:568px">
  <div class="video-tools">
    <div class="video-tool"><svg width="11" height="10" viewBox="0 0 12 11"><path d="M6 10.5L1.2 5.8C-.4 4.2.3 1 3 1c1.3 0 2.3.8 3 1.8C6.7 1.8 7.7 1 9 1c2.7 0 3.4 3.2 1.8 4.8z" fill="#fff"/></svg>LIKE</div>
    <div class="video-tool"><svg width="10" height="10" viewBox="0 0 10 10"><circle cx="5" cy="5" r="4.2" fill="none" stroke="#fff" stroke-width="1.3"/><path d="M5 2.5V5l1.8 1.3" fill="none" stroke="#fff" stroke-width="1.2"/></svg>LATER</div>
    <div class="video-tool"><svg width="11" height="10" viewBox="0 0 11 10"><circle cx="2" cy="5" r="1.6" fill="#fff"/><circle cx="9" cy="1.8" r="1.6" fill="#fff"/><circle cx="9" cy="8.2" r="1.6" fill="#fff"/><path d="M2 5L9 1.8M2 5l7 3.2" stroke="#fff" stroke-width="1"/></svg>SHARE</div>
  </div>
  <div class="video-bar">
    <svg width="202" height="24" viewBox="0 0 202 24"><rect x="12" y="7" width="3" height="10" fill="#fff"/><rect x="18" y="7" width="3" height="10" fill="#fff"/><rect x="42" y="2" width="26" height="9" fill="#fff"/><text x="44" y="9" font-size="6.5" font-family="Open Sans, sans-serif">00:00</text><rect x="42" y="13" width="86" height="5" fill="none" stroke="#666"/><g fill="#666"><rect x="132" y="9" width="1.5" height="8"/><rect x="135" y="9" width="1.5" height="8"/><rect x="138" y="9" width="1.5" height="8"/><rect x="141" y="9" width="1.5" height="8"/><rect x="144" y="9" width="1.5" height="8"/></g><text x="150" y="16" font-size="9" font-weight="700" font-style="italic" fill="#666" font-family="Open Sans, sans-serif">HD</text><path d="M176 8h3M176 8v3M186 8h-3M186 8v3M176 17h3M176 17v-3M186 17h-3M186 17v-3" stroke="#fff" stroke-width="1.4"/></svg>
  </div>
</div>

<h3 class="abs card-title" style="left:96px;top:736px">Most important self development rules</h3>
<p class="abs card-text" style="left:96px;top:756px;width:230px">Proin gravida nibh vel velit auctor aliquet.<br>Aenean sollicitudin, lorem quis bibendum auctor.</p>
<h3 class="abs card-title" style="left:343px;top:736px">20 dating advices for smooth dates</h3>
<p class="abs card-text" style="left:343px;top:756px;width:230px">Proin gravida nibh vel velit auctor aliquet lorem.<br>Aenean sollicitudin, lorem quis.</p>

<!-- agenda -->
<h2 class="abs section-title" style="left:96px;top:813px">AGENDA</h2>
<div class="abs section-link" style="left:500px;top:818px">
  <svg width="12" height="12" viewBox="0 0 12 12"><path d="M6 .5l1.7 3.6 3.8.4-2.9 2.6.8 3.9L6 9 2.6 11l.8-3.9L.5 4.5l3.8-.4z" fill="currentColor"/></svg>All events
</div>

<div class="abs event" style="left:96px;top:850px">
  <div class="event-date"><div class="day">5</div><div class="month">MAY</div></div>
  <div class="event-photo" role="img" aria-label="Photo of a couple laughing outdoors at a seaside event" style="background:linear-gradient(160deg,#9fc4dc,#d9cbb6 60%,#b08a6a)"></div>
</div>
<div class="abs event" style="left:344px;top:850px">
  <div class="event-date"><div class="day">23</div><div class="month">MAY</div></div>
  <div class="event-photo" role="img" aria-label="Photo of a man and a woman chatting at a social meetup" style="background:linear-gradient(160deg,#d8c9ae,#a88e74 55%,#4f4338)"></div>
</div>

<h3 class="abs card-title" style="left:96px;top:943px">Most important self development rules</h3>
<p class="abs card-text" style="left:96px;top:963px;width:230px">Proin gravida nibh vel velit auctor aliquet.Aenean<br>sollicitudin, lorem quis bibendum auctor. Donec<br>quis bibendum auctor.</p>
<div class="abs read-more" style="left:256px;top:1006px">Read more</div>
<h3 class="abs card-title" style="left:344px;top:943px">Most important self development rules</h3>
<p class="abs card-text" style="left:344px;top:963px;width:230px">Proin gravida nibh vel velit auctor aliquet.Aenean<br>sollicitudin, lorem quis bibendum auctor. Donec<br>quis bibendum auctor.</p>
<div class="abs read-more" style="left:504px;top:1006px">Read more</div>

<!-- blog -->
<h2 class="abs section-title" style="left:605px;top:527px">BLOG</h2>
<div class="abs section-link" style="left:724px;top:533px">
  <svg width="12" height="11" viewBox="0 0 12 11"><path d="M6 0C2.7 0 0 2 0 4.6c0 1.4.8 2.6 2 3.4L1.5 11 4.6 9c.4.1.9.1 1.4.1 3.3 0 6-2 6-4.5S9.3 0 6 0z" fill="currentColor"/></svg>All posts
</div>

<div class="abs blog-photo" style="left:608px;top:570px;background:linear-gradient(135deg,#6f4e3a,#c79a5b 45%,#3f3a3a)" role="img" aria-label="Photo of a man and a woman talking in a colourful shop"></div>
<h3 class="abs card-title" style="left:606px;top:683px;width:170px">10 reason why you should flirt with women</h3>
<p class="abs card-text" style="left:606px;top:716px;width:165px">Proin gravida nibh vel velit auctor<br>aliquet. Aenean sollicitudin, lorem<br>quis bibendum auctor.</p>
<div class="abs read-more" style="left:722px;top:760px">Read more</div>

<div class="abs blog-photo" style="left:608px;top:803px;background:linear-gradient(135deg,#8d8f93,#c5c2bd 50%,#4a4644)" role="img" aria-label="Photo of a man and a woman chatting on a city street"></div>
<h3 class="abs card-title" style="left:606px;top:916px;width:170px">Most important self development rules</h3>
<p class="abs card-text" style="left:606px;top:950px;width:165px">Proin gravida nibh vel velit auctor<br>aliquet. Aenean sollicitudin, lorem<br>quis bibendum auctor.</p>
<div class="abs read-more" style="left:722px;top:992px">Read more</div>

<!-- footer -->
<footer class="abs footer">
  <h4 style="left:96px;top:14px">Navigation</h4>
  <span class="link" style="left:96px;top:44px">Services</span>
  <span class="link" style="left:155px;top:44px;text-decoration:underline">Video Gallery</span>
  <span class="link" style="left:96px;top:65px">About Us</span>
  <span class="link" style="left:155px;top:65px">Blog</span>
  <span class="link" style="left:96px;top:87px">Agenda</span>
  <span class="link" style="left:155px;top:87px">Contacts</span>

  <h4 style="left:270px;top:14px">Contacts</h4>
  <svg class="abs" style="left:274px;top:48px" width="9" height="15" viewBox="0 0 9 15"><rect x=".5" y=".5" width="8" height="14" rx="1.5" fill="#4e4e4e"/><rect x="2" y="2.5" width="5" height="8" fill="#8a8a8a"/></svg>
  <span class="link" style="left:298px;top:50px">555 010 2244</span>
  <svg class="abs" style="left:271px;top:85px" width="16" height="11" viewBox="0 0 16 11"><rect x=".5" y=".5" width="15" height="10" fill="#4e4e4e"/><path d="M.5.5l7.5 6 7.5-6" fill="none" stroke="#8a8a8a"/></svg>
  <span class="link" style="left:298px;top:83px;text-decoration:underline">info@brightharbor.example</span>

  <h4 style="left:449px;top:14px">Send us a message</h4>
  <div class="input" style="left:445px;top:34px;width:137px">Name</div>
  <div class="input" style="left:445px;top:63px;width:137px">E-Mail</div>
  <div class="input" style="left:445px;top:92px;width:137px">Subject</div>
  <div class="input" style="left:594px;top:34px;width:154px;height:48px">Your message</div>
  <div class="abs send">Send</div>
</footer>
<div class="abs copyright">All right reserved © Bright Harbor 2013</div>

</body>
</html>
```